Orbit Lane Website - Enabling Omni channel

Slogan : Enabling Omnichannel Sales

1. Sell products via multiple sale channels
2. Access our technology and services to get your products moving through new channels
3. Customise our mobile and web technology platforms to suit your supply chain.

Slogan: Orbit lane – Innovating new business.

Use the content from these websites to create a new one
http://brovanixhq.example/
http://pellow-studio.example/orbitLane02/

Target Market(s)

Business and Coporations who need mobile and web technology or services to increase product sales within their vertical industry. Our case studies show the industries we have worked in; namely: Retail, wholesale, online retail, motor and auto trade. Also have rich experience in Importing and Exporting.

Industry/Entity Type

Retail

Number of Pages Required

3 page

Font styles to use
Sans Serif

Colors
0255a3
ec1f27
9bcb3c
ffffff
0792cd
ffc214

Requirements
Must have
• Punchy headline home page with possible animations or unique and interesting images

```html
<!DOCTYPE html>
<html lang="en">
<head>
<meta charset="utf-8">
<title>Orbit Lane – Innovating new business</title>
<link href="https://fonts.googleapis.com/css2?family=Open+Sans:ital,wght@0,400;0,600;0,700;1,400&family=Raleway:wght@400;500;600;700&display=swap" rel="stylesheet">
<style>
:root{
  --brand-blue:#0255a3;
  --sky-blue:#0792cd;
  --red:#ec1f27;
  --green:#9bcb3c;
  --yellow:#ffc214;
  --orange:#f7a21b;
  --white:#ffffff;
  --ink:#3a3a3a;
  --grey:#8a8a8a;
  --navy:#1d2f55;
  --heading:"Raleway",sans-serif;
  --body:"Open Sans",sans-serif;
}
*{box-sizing:border-box;margin:0;padding:0}
html,body{width:1200px;height:2564px;overflow:hidden;background:var(--white)}
body{font-family:var(--body);color:var(--ink);position:relative}
section,header,footer{position:relative;width:1200px}
.abs{position:absolute}

/* header */
.site-header{height:89px;background:var(--white)}
.brand{left:185px;top:20px}
.brand-name{font-family:var(--heading);font-weight:700;font-size:34px;color:var(--brand-blue);line-height:1;letter-spacing:-.5px}
.brand-tagline{font-family:var(--heading);font-size:13px;color:var(--brand-blue);margin-top:3px;padding-left:60px}
.main-nav{top:37px;left:0;width:1200px;font-family:var(--heading);font-weight:500;font-size:13.5px;color:#333}
.main-nav span{position:absolute;white-space:nowrap}
.main-nav .is-active{color:var(--brand-blue)}

/* hero */
.hero{height:497px;background:var(--white)}
.hero-photo{inset:0;background:linear-gradient(100deg,#3e4146 0%,#6f7276 35%,#585a5e 65%,#2f3033 100%);clip-path:polygon(0 0,100% 0,100% 408px,50% 497px,0 424px)}
.hero-shade{inset:0;background:rgba(20,22,28,.28);clip-path:polygon(0 0,100% 0,100% 408px,50% 497px,0 424px)}
.hero-title{top:162px;width:1200px;text-align:center;color:var(--white);font-family:var(--heading);font-weight:700;font-size:39px;letter-spacing:.5px}
.hero-sub{top:212px;width:1200px;text-align:center;color:var(--white);font-family:var(--heading);font-weight:700;font-size:20px;letter-spacing:.5px}
.btn-learn{left:531px;top:260px;width:137px;height:36px;background:var(--red);color:var(--white);font-family:var(--heading);font-weight:700;font-size:13px;display:flex;align-items:center;justify-content:center}
.slider-dots{left:567px;top:460px;display:flex;gap:4px}
.slider-dots i{width:11px;height:11px;border-radius:50%;background:var(--white);border:1.5px solid var(--white)}
.slider-dots i:first-child{background:transparent}

/* offers */
.offers{height:301px}
.offer{width:300px;text-align:center}
.offer-icon{width:86px;height:86px;border-radius:50%;border:2px solid #e2e2e2;margin:0 auto;display:flex;align-items:center;justify-content:center}
.offer-title{font-family:var(--heading);font-size:19px;margin-top:22px}
.offer-text{font-size:11px;color:var(--grey);line-height:21px;margin-top:4px;padding:0 70px}
.btn-small{display:inline-block;width:89px;height:24px;line-height:24px;color:var(--white);font-family:var(--heading);font-weight:700;font-size:9.5px;margin-top:10px}
.offer--brand .offer-title{color:var(--sky-blue)} .offer--brand .btn-small{background:var(--sky-blue)}
.offer--product .offer-title{color:var(--green)} .offer--product .btn-small{background:var(--green)}
.offer--service .offer-title{color:var(--yellow)} .offer--service .btn-small{background:var(--yellow)}

/* bundle */
.bundle{height:366px;background:linear-gradient(160deg,#1a9ad6 0%,#0a86c7 50%,#0c7fc1 100%);color:var(--white)}
.bundle-title{top:77px;width:1200px;text-align:center;font-family:var(--heading);font-size:29px;letter-spacing:.5px}
.bundle-sub{top:122px;width:1200px;text-align:center;font-family:var(--heading);font-size:20px}
.bundle-item{font-size:12.5px;display:flex;align-items:center;gap:9px;white-space:nowrap}

/* marketing */
.marketing{height:388px;background:linear-gradient(90deg,#223961 0%,#2c4a79 55%,#1f3358 100%);color:var(--white)}
.marketing-title{left:197px;top:86px;font-family:var(--heading);font-size:29px}
.marketing-sub{left:201px;top:126px;width:400px;font-family:var(--heading);font-size:18px;line-height:24px}
.marketing-list{left:201px;top:186px;list-style:none;font-size:13px}
.marketing-list li{height:30.5px;display:flex;gap:14px}
.device{left:564px;top:65px;width:467px;height:241px;border-radius:14px 14px 4px 4px;background:linear-gradient(180deg,#dcdfe3,#c3c7cc);border:6px solid #cfd2d6}
.device-base{left:560px;top:305px;width:475px;height:10px;border-radius:0 0 10px 10px;background:#d9dbde}

/* next steps */
.next-steps{height:372px}
.next-photo{left:222px;top:54px;width:357px;height:217px;background:linear-gradient(135deg,#d9c58a,#c9d4de 55%,#7fa7c9)}
.next-title{left:646px;top:64px;font-family:var(--heading);font-size:22px;color:#444}
.next-text{left:646px;top:100px;width:370px;font-size:12.3px;line-height:23px;color:#777}
.btn-outline{left:648px;top:229px;width:119px;height:39px;border:2px solid var(--sky-blue);color:var(--sky-blue);font-family:var(--heading);font-size:12px;display:flex;align-items:center;justify-content:center}

/* stories */
.stories{height:289px;background:linear-gradient(180deg,#f8b91c,#f5b017);color:var(--white)}
.stories-title{top:56px;width:1200px;text-align:center;font-family:var(--heading);font-size:29px}
.stories-text{left:263px;top:102px;width:676px;text-align:center;font-style:italic;font-size:13px;line-height:22px}
.btn-stories{left:514px;top:205px;width:176px;height:41px;background:var(--orange);border:2px solid var(--white);font-family:var(--heading);font-size:13px;display:flex;align-items:center;justify-content:center}

/* footer */
.site-footer{height:262px;background:var(--brand-blue);color:var(--white)}
.footer-col{top:36px}
.footer-col h4{font-family:var(--heading);font-weight:700;font-size:15px;letter-spacing:.5px;margin-bottom:10px}
.footer-col li{list-style:none;font-size:11px;line-height:19.5px}
.social{display:flex;gap:4px;margin-top:8px}
.social i{width:27px;height:27px;border-radius:50%;border:1.5px solid var(--white)}
.footer-brand{left:872px;top:70px;font-family:var(--heading);font-weight:700;font-size:32px;letter-spacing:-.5px}
.footer-rule{left:208px;top:205px;width:826px;height:1px;background:rgba(255,255,255,.35)}
.copyright{top:222px;width:1200px;text-align:center;font-size:11px;color:rgba(255,255,255,.7)}
</style>
</head>
<body>

<header class="site-header">
  <div class="brand abs">
    <div class="brand-name">Orbit Lane</div>
    <div class="brand-tagline">Innovating new business</div>
  </div>
  <nav class="main-nav abs">
    <span class="is-active" style="left:500px">HOME</span>
    <span style="left:566px">ABOUT US</span>
    <span style="left:660px">SERVICES</span>
    <span style="left:749px">SOLUTION</span>
    <span style="left:843px">TESTIMONIAL</span>
    <span style="left:960px">CONTACT</span>
  </nav>
</header>

<section class="hero">
  <div class="hero-photo abs" role="img" aria-label="Photo of a team working together on laptops in an office"></div>
  <div class="hero-shade abs"></div>
  <h1 class="hero-title abs">CLASS APTENT TACITI SOCIOSQU</h1>
  <p class="hero-sub abs">MAECENAS ALIQUET VELIT VEL TURPIS</p>
  <a class="btn-learn abs">LEARN MORE</a>
  <div class="slider-dots abs"><i></i><i></i><i></i><i></i></div>
</section>

<section class="offers">
  <div class="offer offer--brand abs" style="left:182px;top:31px">
    <div class="offer-icon">
      <svg width="40" height="44" viewBox="0 0 40 44"><path d="M34 2C14 6 4 18 6 40 26 36 36 22 34 2Z" fill="#0792cd"/><path d="M8 38 28 10" stroke="#fff" stroke-width="2"/></svg>
    </div>
    <h3 class="offer-title">Are Your a Brand</h3>
    <p class="offer-text">Mauris neque metus malesuada nec ultricies sit amet porttitor mattis</p>
    <a class="btn-small">READ MORE</a>
  </div>
  <div class="offer offer--product abs" style="left:452px;top:31px">
    <div class="offer-icon">
      <svg width="44" height="44" viewBox="0 0 44 44"><path d="M22 4 40 13 22 22 4 13Z" fill="#9bcb3c"/><path d="M4 17 20 25V42L4 34Z M40 17 24 25V42L40 34Z" fill="#9bcb3c"/></svg>
    </div>
    <h3 class="offer-title">Do You Have Products?</h3>
    <p class="offer-text">Mauris neque metus malesuada nec ultricies sit amet porttitor mattis</p>
    <a class="btn-small">READ MORE</a>
  </div>
  <div class="offer offer--service abs" style="left:730px;top:31px">
    <div class="offer-icon">
      <svg width="46" height="46" viewBox="0 0 46 46"><circle cx="18" cy="26" r="11" fill="none" stroke="#ffc214" stroke-width="6" stroke-dasharray="4 3"/><circle cx="18" cy="26" r="5" fill="none" stroke="#ffc214" stroke-width="3"/><circle cx="34" cy="12" r="7" fill="none" stroke="#ffc214" stroke-width="4" stroke-dasharray="3 2"/></svg>
    </div>
    <h3 class="offer-title">Do You Offer a Service?</h3>
    <p class="offer-text">Mauris neque metus malesuada nec ultricies sit amet porttitor mattis</p>
    <a class="btn-small">READ MORE</a>
  </div>
</section>

<section class="bundle">
  <h2 class="bundle-title abs">AWESOME SERVICE BUNDLE</h2>
  <p class="bundle-sub abs">Incorporate the latest hardware devices and tags to boost business</p>
  <div class="bundle-item abs" style="left:198px;top:192px"><svg width="17" height="17" viewBox="0 0 17 17"><circle cx="8.5" cy="8.5" r="8.5" fill="#fff"/><path d="M4.5 8.8 7.3 11.5 12.5 5.8" fill="none" stroke="#0a86c7" stroke-width="2"/></svg>Proxi beacons – enhance customer’s in-store experience (Pomely)</div>
  <div class="bundle-item abs" style="left:198px;top:222px"><svg width="17" height="17" viewBox="0 0 17 17"><circle cx="8.5" cy="8.5" r="8.5" fill="#fff"/><path d="M4.5 8.8 7.3 11.5 12.5 5.8" fill="none" stroke="#0a86c7" stroke-width="2"/></svg>NFC tags – enhance customer’s in-store experience (Selvora)</div>
  <div class="bundle-item abs" style="left:653px;top:196px"><svg width="17" height="17" viewBox="0 0 17 17"><circle cx="8.5" cy="8.5" r="8.5" fill="#fff"/><path d="M4.5 8.8 7.3 11.5 12.5 5.8" fill="none" stroke="#0a86c7" stroke-width="2"/></svg>RFId tags- track global supply chains</div>
  <div class="bundle-item abs" style="left:653px;top:226px"><svg width="17" height="17" viewBox="0 0 17 17"><circle cx="8.5" cy="8.5" r="8.5" fill="#fff"/><path d="M4.5 8.8 7.3 11.5 12.5 5.8" fill="none" stroke="#0a86c7" stroke-width="2"/></svg>Video and movement sensors – for in-store retail insights</div>
</section>

<section class="marketing" role="region" aria-label="Marketing and sales">
  <h2 class="marketing-title abs">MARKETING AND SALES</h2>
  <p class="marketing-sub abs">We go to the ends of the earth to get your products selling.</p>
  <ul class="marketing-list abs">
    <li><span>›</span>Broaden Customer reach with multi-channel Marketing.</li>
    <li><span>›</span>Be where Customers are by Selling Online and on Mobile.</li>
    <li><span>›</span>Be top of your Customer’s mind using Loyalty.</li>
  </ul>
  <div class="device abs" role="img" aria-label="Laptop showing a sketch of business growth charts above a city skyline"></div>
  <div class="device-base abs"></div>
</section>

<section class="next-steps">
  <div class="next-photo abs" role="img" aria-label="Photo of two colleagues reviewing work on a laptop"></div>
  <h2 class="next-title abs">WHAT TO DO NOW</h2>
  <p class="next-text abs">If any of these situations are what you need, you’re not alone. Many suppliers and manufacturers face these challenges. Orbit Lane can help you create a marketing and sales plan for your situation, often incorporating our existing in-store and factory direct model using the Vantrel supply chain.</p>
  <a class="btn-outline abs">VIEW MORE</a>
</section>

<section class="stories">
  <h2 class="stories-title abs">Sucess Stories</h2>
  <p class="stories-text abs">Fashion-apparel brand, Orbit Lane acquired the brand, intellectual property, stock and trading in June 2014. The brand consisted of 80 SKU’s and sold off a website. In order to increase the sales, KRV an American retailer assisted in the exporting of the product. The substantial amount of inventory was sold to KRV and an ongoing export business was established.</p>
  <a class="btn-stories abs">More Success Stories</a>
</section>

<footer class="site-footer">
  <div class="footer-col abs" style="left:208px"><h4>COMPANY</h4><ul><li>What We Do</li><li>How it Works</li><li>Who</li><li>Where</li></ul></div>
  <div class="footer-col abs" style="left:343px"><h4>SUBLINKS</h4><ul><li>Sed metus augue</li><li>Convallis et vehicula</li><li>Pulvinar eu</li><li>Ante integer orci</li></ul></div>
  <div class="footer-col abs" style="left:513px"><h4>RESOURCES</h4><ul><li>Support</li><li>Term &amp; Condition</li><li>Privacy Policy</li></ul></div>
  <div class="footer-col abs" style="left:678px"><h4>FOLLOW US</h4><ul><li>Get in touch with us anyhwere</li></ul><div class="social"><i></i><i></i><i></i><i></i></div></div>
  <div class="footer-brand abs">Orbit Lane</div>
  <div class="footer-rule abs"></div>
  <p class="copyright abs">© 2016 Company Name&nbsp; All right reserved</p>
</footer>

</body>
</html>
```